Business Card Design

VEGETABLE FARMING OPERATION PRIMARY CROPS SPINACH,SPRING MIX, HEAD LETTUCE, ROMAINE, BRUSSEL SPROUTS, VELVET TOP GREENS BROCCOLI CAULIFLOWER CELERY NEED A Business card THAT REPRESENTS SOME OF THOSE CROPS AY IDEAS WELCOME..

The business is vegetable farming spinach spring mix head lettuce romaine broccoli brussel sprouts celery carrots target audience is potential shippers of products week spring mix spinach harvesting as well. I colors in mind just need a card that's original

Industry/Entity Type

Farming

Contact Information for Business Card

R&K FARMS LLC BRIDGEWOOD FARMS LLC

```html
<!DOCTYPE html>
<html lang="en">
<head>
<meta charset="utf-8">
<title>R&amp;K Farms Business Card</title>
<link rel="stylesheet" href="https://fonts.googleapis.com/css2?family=Oxygen:wght@300;400&display=swap">
<style>
  :root {
    --page-bg: #ecebe6;
    --card-white: #f7f7f7;
    --brand-green: #0fa556;
    --brand-green-light: #1fc47a;
    --text-green: #17a055;
    --circle-white: #f4f4f4;
    --veg-light: #9ccf6a;
    --veg-dark: #2f7d32;
    --cauliflower: #e9e4cf;
  }
  * { margin: 0; padding: 0; box-sizing: border-box; }
  html, body {
    width: 1200px; height: 900px; overflow: hidden;
    background: var(--page-bg);
  }
  .stage {
    width: 1200px; height: 900px;
    display: flex; align-items: center; justify-content: center;
  }
  .business-card {
    position: relative;
    width: 735px; height: 420px;
    border-radius: 26px;
    overflow: hidden;
    display: flex;
    box-shadow: 0 14px 34px rgba(0,0,0,0.18);
  }
  .card-info {
    width: 330px; height: 100%;
    background: var(--card-white);
    padding: 46px 0 0 48px;
    font-family: "Oxygen", sans-serif;
    color: var(--text-green);
  }
  .company-names { font-size: 25px; font-weight: 400; line-height: 1.22; letter-spacing: 0.2px; }
  .contact-block { margin-top: 96px; font-weight: 300; }
  .person-name { font-size: 25px; letter-spacing: 1px; line-height: 1.2; }
  .person-role { font-size: 20px; line-height: 1.3; }
  .contact-lines { margin-top: 26px; font-size: 20px; line-height: 1.3; }
  .card-crops {
    flex: 1; height: 100%;
    background: linear-gradient(135deg, var(--brand-green-light) 0%, var(--brand-green) 55%, #0b9a4e 100%);
  }
  .card-crops svg { display: block; }
</style>
</head>
<body>
<main class="stage">
  <article class="business-card">
    <section class="card-info">
      <h1 class="company-names">R&amp;K FARMS LLC<br>BRIDGEWOOD FARMS LLC</h1>
      <div class="contact-block">
        <p class="person-name">NAME</p>
        <p class="person-role">Designation</p>
        <div class="contact-lines">
          <p>123-456-7890</p>
          <p>name@rkfarmsmail.com</p>
          <p>www.rkfarmsfresh.com</p>
        </div>
      </div>
    </section>
    <section class="card-crops">
      <svg width="405" height="420" viewBox="0 0 405 420">
        <g class="crop-badge">
          <circle cx="95" cy="95" r="46" fill="var(--circle-white)"/>
          <circle cx="95" cy="95" r="30" fill="var(--veg-light)" role="img" aria-label="Celery stalks photo"/>
        </g>
        <g class="crop-badge">
          <circle cx="210" cy="60" r="46" fill="var(--circle-white)"/>
          <circle cx="210" cy="60" r="30" fill="var(--veg-dark)" role="img" aria-label="Spinach leaves photo"/>
        </g>
        <g class="crop-badge">
          <circle cx="330" cy="95" r="46" fill="var(--circle-white)"/>
          <circle cx="330" cy="95" r="30" fill="#5f9e3c" role="img" aria-label="Brussels sprouts photo"/>
        </g>
        <g class="crop-badge">
          <circle cx="60" cy="210" r="46" fill="var(--circle-white)"/>
          <circle cx="60" cy="210" r="30" fill="var(--veg-light)" role="img" aria-label="Head lettuce photo"/>
        </g>
        <g class="crop-badge">
          <circle cx="180" cy="190" r="46" fill="var(--circle-white)"/>
          <circle cx="180" cy="190" r="30" fill="#4b6b2a" role="img" aria-label="Spring mix salad photo"/>
        </g>
        <g class="crop-badge">
          <circle cx="300" cy="215" r="46" fill="var(--circle-white)"/>
          <circle cx="300" cy="215" r="30" fill="#3e8a35" role="img" aria-label="Broccoli photo"/>
        </g>
        <g class="crop-badge">
          <circle cx="95" cy="325" r="46" fill="var(--circle-white)"/>
          <circle cx="95" cy="325" r="30" fill="var(--cauliflower)" role="img" aria-label="Cauliflower photo"/>
        </g>
        <g class="crop-badge">
          <circle cx="215" cy="320" r="46" fill="var(--circle-white)"/>
          <circle cx="215" cy="320" r="30" fill="#6fb44a" role="img" aria-label="Romaine lettuce photo"/>
        </g>
        <g class="crop-badge">
          <circle cx="335" cy="340" r="46" fill="var(--circle-white)"/>
          <circle cx="335" cy="340" r="30" fill="var(--veg-dark)" role="img" aria-label="Velvet top greens photo"/>
        </g>
      </svg>
    </section>
  </article>
</main>
</body>
</html>
```